Venue Booking Site

I would like a venue directory and booking website designed. The idea is that end users will come to the site to find venues for weddings, parties, events etc. They will be able to find the venue based on many criteria, the most important ones are availability and location - they will be able to see in real time which venues are available for the desired dates and areas.

Venues will be able to use the website as a reservation management tool, receive payments for bookings through the site and be able to manage bookings on the go. This will be made into an app. It needs to be developed in bootstrap. Brand name to be used: Mirqona. Venue, place and space bookings.

Target audience - end users - anyone who is looking for a venue. For Community members it will provide an easy way to find a suitable venue
Outline what dates and times the venue is available
Outline costs involved in booking the venue
Search via many other criteria
It will allow the customer to book and pay for the venue online in one smooth process

Clients: Venue managers - particularly focussing on not for profit businesses eg, GHAs, community hall managers, small business managers. These people typically use paper based systems yet and do not use websites so it needs to be very user friendly. Future growth to restaurants, pubs, event venues who have a stronger familiarity with computers and who might already use their own booking management tool - so this needs to be able to link in with their system.

What need will this meet for venue managers:
This tool provides venues with greater visibility, promotion and advertising of their venue
This allows more customers to find them and book with them
This tool will be offered to not-for-profit venue managers for free to better connect them to the community
This means greater profit for these community venues
This means more revenue and jobs created in these communities

Sample of the layout / contents attached. This is not a complete site map as yet as it is a work in progress for final pages.

Small Business

5+ page

Sans Serif

eb2027

• This is a psd file only - one template for each different section, home page, search page, detailed page view, admin back end
• does not need to be coded.
• Note, the golden lantern logo jpeg files were files we were toying with using for this project- but I am happy to use the main mirqona logo- I will let you decide.

```html
<!DOCTYPE html>
<html lang="en">
<head>
<meta charset="utf-8">
<title>Mirqona Venue Booking</title>
<link href="https://fonts.googleapis.com/css2?family=Open+Sans:wght@400;600&family=Roboto:wght@400;500&display=swap" rel="stylesheet">
<style>
:root{
  --red:#eb2027;
  --dark:#35373a;
  --darker:#2f3133;
  --text:#555;
  --muted:#777;
  --line:#e4e4e4;
  --page:#f3f3f3;
  --white:#fff;
  --star:#f5a623;
}
*{box-sizing:border-box;margin:0;padding:0}
html,body{width:1074px;height:1200px;overflow:hidden}
body{position:relative;background:var(--page);font-family:"Open Sans",sans-serif;color:var(--text)}
.abs{position:absolute}
/* header */
.site-header{left:0;top:0;width:1074px;height:139px;background:var(--white)}
.brand{left:45px;top:44px;display:flex;align-items:center;gap:10px}
.brand-mark{width:26px;height:26px;border-radius:50%;background:var(--red)}
.brand-name{font-family:"Roboto",sans-serif;font-size:38px;font-weight:500;color:var(--red);letter-spacing:.5px}
.list-venue{left:663px;top:56px;width:119px;height:32px;background:var(--dark);color:#fff;font-family:"Roboto",sans-serif;font-size:15px;display:flex;align-items:center;justify-content:center;border-radius:2px}
.field{top:44px;width:100px;height:27px;border:1px solid #ccc;border-radius:14px;font-size:9.5px;color:#888;display:flex;align-items:center;gap:7px;padding-left:12px}
.remember{left:810px;top:89px;font-size:9.5px;color:#888;display:flex;align-items:center;gap:6px}
.remember span{width:9px;height:9px;border:1px solid #aaa;border-radius:2px}
.login{left:916px;top:82px;width:93px;height:27px;background:var(--red);color:#fff;border-radius:14px;font-family:"Roboto",sans-serif;font-size:14px;display:flex;align-items:center;justify-content:center}
/* nav */
.main-nav{left:0;top:139px;width:1074px;height:53px;background:var(--dark);display:flex;justify-content:center}
.main-nav a{color:#fff;text-decoration:none;font-family:"Roboto",sans-serif;font-size:14px;display:flex;align-items:center;padding:0 26px;border-right:1px solid #2b2d30}
.main-nav a:last-child{border-right:0}
.nav-shadow{left:210px;top:192px;width:654px;height:24px}
/* toolbar */
.refine-title{left:44px;top:238px;font-size:16px;color:#555}
.sort-bar{left:302px;top:235px;font-size:12px;color:#666;display:flex;align-items:center;gap:14px}
.sort-bar strong{font-weight:400;font-size:16px;color:#555}
.view-btn{top:228px;width:30px;height:29px;background:#e2e2e2;display:flex;align-items:center;justify-content:center}
/* sidebar */
.filters{left:45px;top:273px;width:233px;height:470px;background:var(--white);border:1px solid var(--line);list-style:none}
.filters li{height:30.7px;border-bottom:1px solid #eee;display:flex;align-items:center;font-size:11px;color:#555;padding-left:13px;gap:12px}
.filters li:last-child{border-bottom:0}
.filters li::before{content:"";width:8px;height:8px;border-radius:50%;background:var(--red);box-shadow:inset 0 0 0 2px var(--red),inset 0 0 0 3px #fff}
/* cards */
.venue-card{width:225px;height:320px;background:#f9f9f9;border:1px solid var(--line)}
.venue-photo{height:141px}
.venue-body{padding:13px 14px 0}
.venue-title{font-family:"Roboto",sans-serif;font-size:14px;color:#333;font-weight:400}
.venue-meta{margin-top:8px;display:flex;gap:18px;align-items:center}
.stars{color:var(--star);font-size:10px;letter-spacing:-.5px}
.stars i{font-style:normal;color:#bbb}
.price{font-family:"Roboto",sans-serif;font-size:11.5px;color:var(--red)}
.venue-text{margin-top:8px;font-size:10px;line-height:18.5px;color:#666;text-align:justify}
.book-btn{margin-top:12px;width:89px;height:30px;border:1px solid #ccc;border-radius:15px;background:#fff;color:var(--red);font-family:"Roboto",sans-serif;font-size:12px;display:flex;align-items:center;justify-content:center}
/* footer */
.site-footer{left:0;top:979px;width:1074px;height:174px;background:#f8f8f8}
.divider{top:979px;width:1px;height:174px;background:#ececec}
.foot-h{font-family:"Roboto",sans-serif;font-size:13px;color:var(--red)}
.foot-brand{left:45px;top:994px;font-family:"Roboto",sans-serif;font-size:16px;color:var(--red)}
.foot-addr{left:46px;top:1025px;font-size:11px;line-height:18.5px;color:#555}
.call{left:45px;top:1071px;font-size:16px;color:#666}
.phone{left:45px;top:1094px;font-family:"Roboto",sans-serif;font-size:19px;color:var(--red)}
.foot-links{left:273px;top:1031px;list-style:none;font-size:11px;line-height:18.5px;color:#555}
.post-photo{left:442px;top:1029px;width:113px;height:94px}
.post-text{left:565px;top:1025px;width:181px;font-size:10px;line-height:18.5px;color:#666;text-align:justify}
.newsletter{left:829px;top:1031px;width:185px;height:30px;background:#fff;border:1px solid #eee}
.social{top:1098px;width:29px;height:29px;border-radius:50%;background:#ee4656}
.bottom-bar{left:0;top:1153px;width:1074px;height:47px;background:var(--dark);color:#fff;font-family:"Roboto",sans-serif;font-size:10px}
</style>
</head>
<body>
<header class="abs site-header">
  <div class="abs brand"><span class="brand-mark"></span><span class="brand-name">mirqona</span></div>
  <div class="abs list-venue">List My venue</div>
  <div class="abs field" style="left:805px"><svg width="8" height="8" viewBox="0 0 8 8"><circle cx="4" cy="2.3" r="2" fill="#999"/><path d="M0 8c0-3 8-3 8 0z" fill="#999"/></svg>Username</div>
  <div class="abs field" style="left:913px"><svg width="8" height="8" viewBox="0 0 8 8"><rect x="1" y="3.5" width="6" height="4.5" fill="#999"/><path d="M2.3 3.5V2.3a1.7 1.7 0 0 1 3.4 0v1.2" stroke="#999" fill="none"/></svg>Password</div>
  <div class="abs remember"><span></span>Remember Me</div>
  <div class="abs login">LOGIN</div>
</header>
<nav class="abs main-nav">
  <a>Home</a><a>Venues</a><a>News &amp; Offers</a><a>Inspiration</a><a>Services</a><a>FAQs</a><a>Contact Us</a>
</nav>
<svg class="abs nav-shadow" viewBox="0 0 654 24"><defs><radialGradient id="sh" cx=".5" cy="0" r=".5"><stop offset="0" stop-color="#000" stop-opacity=".22"/><stop offset="1" stop-color="#000" stop-opacity="0"/></radialGradient></defs><ellipse cx="327" cy="0" rx="327" ry="24" fill="url(#sh)"/></svg>

<div class="abs refine-title">Refine Search :</div>
<div class="abs sort-bar"><strong>Sort by :</strong>Rating<span>|</span>Distance<span>|</span>Price Availability<span>|</span>Map View</div>
<div class="abs view-btn" style="left:949px"><svg width="16" height="12"><g fill="#fff"><rect y="0" width="3" height="2"/><rect x="5" y="0" width="11" height="2"/><rect y="5" width="3" height="2"/><rect x="5" y="5" width="11" height="2"/><rect y="10" width="3" height="2"/><rect x="5" y="10" width="11" height="2"/></g></svg></div>
<div class="abs view-btn" style="left:985px"><svg width="16" height="12"><g fill="#fff"><rect width="16" height="2"/><rect y="5" width="16" height="2"/><rect y="10" width="16" height="2"/></g></svg></div>

<ul class="abs filters">
  <li>Venue Type</li><li>Venue Size</li><li>Ceiling Height</li><li>Venue entry door width</li><li>Resource type</li><li>Audio visual requirements</li><li>Entertainment</li><li>Facilities</li><li>Decorations</li><li>Transportation options</li><li>Staff</li><li>Parking spaces</li><li>Packages available –</li><li>Customer rating</li><li>Donation partner</li>
</ul>

<article class="abs venue-card" style="left:302px;top:272px">
  <div class="venue-photo" role="img" aria-label="Modern house with swimming pool, fire pit and palm trees" style="background:linear-gradient(180deg,#cfe3f2 0%,#e8e4da 45%,#5cc3dc 75%,#8a7a66 100%)"></div>
  <div class="venue-body"><h3 class="venue-title">Sed ut perspiciatis unde omnis</h3><div class="venue-meta"><span class="stars">★★★<i>☆☆</i></span><span class="price">$2010.00</span></div><p class="venue-text">Lorem ipsum dolor sit amet, consectetur adipiscing elit, sed do eiusmod tempor incididunt ut labore et</p><div class="book-btn">Book Now</div></div>
</article>
<article class="abs venue-card" style="left:548px;top:272px">
  <div class="venue-photo" role="img" aria-label="Two-storey family house with garage and green lawn" style="background:linear-gradient(180deg,#5e9fd8 0%,#b9a58e 45%,#d9d4c8 70%,#4f8a34 100%)"></div>
  <div class="venue-body"><h3 class="venue-title">Sed ut perspiciatis unde omnis</h3><div class="venue-meta"><span class="stars">★★★<i>☆☆</i></span><span class="price">$2010.00</span></div><p class="venue-text">Lorem ipsum dolor sit amet, consectetur adipiscing elit, sed do eiusmod tempor incididunt ut labore et</p><div class="book-btn">Book Now</div></div>
</article>
<article class="abs venue-card" style="left:790px;top:272px">
  <div class="venue-photo" role="img" aria-label="Victorian style house with porch and garden" style="background:linear-gradient(180deg,#8fb6d8 0%,#a8a58c 40%,#c9c3b0 65%,#5b9a3a 100%)"></div>
  <div class="venue-body"><h3 class="venue-title">Sed ut perspiciatis unde omnis</h3><div class="venue-meta"><span class="stars">★★★<i>☆☆</i></span><span class="price">$2010.00</span></div><p class="venue-text">Lorem ipsum dolor sit amet, consectetur adipiscing elit, sed do eiusmod tempor incididunt ut labore et</p><div class="book-btn">Book Now</div></div>
</article>
<article class="abs venue-card" style="left:302px;top:617px">
  <div class="venue-photo" role="img" aria-label="Terracotta tiled roofs against a blue sky" style="background:linear-gradient(160deg,#5a9ad6 0%,#a9cbe8 35%,#d9643f 60%,#e8b8b0 100%)"></div>
  <div class="venue-body"><h3 class="venue-title">Sed ut perspiciatis unde omnis</h3><div class="venue-meta"><span class="stars">★★★<i>☆☆</i></span><span class="price">$2010.00</span></div><p class="venue-text">Lorem ipsum dolor sit amet, consectetur adipiscing elit, sed do eiusmod tempor incididunt ut labore et</p><div class="book-btn">Book Now</div></div>
</article>
<article class="abs venue-card" style="left:548px;top:617px">
  <div class="venue-photo" role="img" aria-label="Family standing in front of a brick house" style="background:linear-gradient(180deg,#c8d8e6 0%,#a29a90 40%,#8a9a6a 70%,#4e8a2e 100%)"></div>
  <div class="venue-body"><h3 class="venue-title">Sed ut perspiciatis unde omnis</h3><div class="venue-meta"><span class="stars">★★★<i>☆☆</i></span><span class="price">$2010.00</span></div><p class="venue-text">Lorem ipsum dolor sit amet, consectetur adipiscing elit, sed do eiusmod tempor incididunt ut labore et</p><div class="book-btn">Book Now</div></div>
</article>
<article class="abs venue-card" style="left:790px;top:617px">
  <div class="venue-photo" role="img" aria-label="Grey sided two-storey house with lawn" style="background:linear-gradient(180deg,#b9c3cc 0%,#7d847c 45%,#8e948a 70%,#5a8f35 100%)"></div>
  <div class="venue-body"><h3 class="venue-title">Sed ut perspiciatis unde omnis</h3><div class="venue-meta"><span class="stars">★★★<i>☆☆</i></span><span class="price">$2010.00</span></div><p class="venue-text">Lorem ipsum dolor sit amet, consectetur adipiscing elit, sed do eiusmod tempor incididunt ut labore et</p><div class="book-btn">Book Now</div></div>
</article>

<footer class="abs site-footer"></footer>
<div class="abs divider" style="left:236px"></div>
<div class="abs divider" style="left:399px"></div>
<div class="abs divider" style="left:784px"></div>
<div class="abs foot-brand">Mirqona Bookings</div>
<div class="abs foot-addr">12 Tallow Lane Norwood VIC<br>info@bookings.mirqona.com.au</div>
<div class="abs call">Call Now</div>
<div class="abs phone">03 5550 1427</div>
<div class="abs foot-h" style="left:275px;top:1000px">INFORMATION</div>
<ul class="abs foot-links"><li>Home</li><li>Venues</li><li>News &amp; Offers</li><li>Inspiration</li><li>Services</li></ul>
<div class="abs foot-h" style="left:443px;top:1000px">RECENT POST</div>
<div class="abs post-photo" role="img" aria-label="Two-storey house with garage" style="background:linear-gradient(180deg,#6fa6dc 0%,#d8c79c 55%,#7a8f4a 100%)"></div>
<p class="abs post-text">Lorem ipsum dolor sit amet, consectur adipiscing elit, sed do eiusmod tempor incididunt ut labore et dolore magna aliqua. Ut enim ad minim veniam, quis nostrud exercitation ullamco</p>
<div class="abs foot-h" style="left:829px;top:1000px">NEWSLETTER</div>
<div class="abs newsletter"><svg class="abs" style="left:168px;top:11px" width="6" height="8"><path d="M1 1l3 3-3 3" stroke="#555" stroke-width="1.5" fill="none"/></svg></div>
<div class="abs foot-h" style="left:826px;top:1074px">FOLLOW US</div>
<div class="abs social" style="left:823px"></div>
<div class="abs social" style="left:860px"></div>
<div class="abs social" style="left:897px"></div>

<div class="abs bottom-bar">
  <span class="abs" style="left:49px;top:18px">©2013 - 2014 Mirqona., All Rights Reserved.</span>
  <span class="abs" style="left:743px;top:18px">Terms of Service | Privacy Policy</span>
</div>
</body>
</html>
```